International sports company needs packaging design for color box

We need this box for our yoga mats which we will sell online. This mat is very high quality and 100% environmentally friendly. The yoga mat comes in a stylish yoga bag that will be in the box.

Yoga enthusiasts, athletes, gymnasts, actually all people who do sporting activities and value environmental friendliness will be the contact group

The logo should be visible in any case. The creator is free to choose whether to use only the complete logo or the complete logo with the emblem. In terms of style, it should be reminiscent of a packaging box from Zorvik's Valmox. Be as timeless, modern and elegant as possible. If an environmentally friendly detail can be added, this would certainly be a plus. Color should be black / white / gray.

Target Market(s)

Germany

Requirements
Must have
• Size for the color box should be 13x13x61.5 cm.

```html
<!DOCTYPE html>
<html lang="en">
<head>
<meta charset="utf-8">
<title>K.E.L.T Yoga Mat Box</title>
<link rel="stylesheet" href="https://fonts.googleapis.com/css2?family=Arimo:wght@700&display=swap">
<style>
  :root {
    --canvas-bg: #e4e4e4;
    --panel-white: #f7f7f7;
    --panel-black: #0f0f0f;
    --type-light: #d4d4d4;
    --type-dark: #111111;
    --edge: #c9c9c9;
  }
  * { margin: 0; padding: 0; box-sizing: border-box; }
  html, body {
    width: 1200px;
    height: 1200px;
    overflow: hidden;
    background: var(--canvas-bg);
  }
  .canvas {
    width: 1200px;
    height: 1200px;
    display: flex;
    flex-direction: column;
    align-items: center;
    justify-content: center;
    gap: 0;
  }
  .box-face {
    width: 1000px;
    height: 212px;
    display: flex;
    border: 1px solid var(--edge);
  }
  .box-face + .box-face { border-top: none; }
  .face-emblem-zone {
    width: 300px;
    background: var(--panel-white);
    display: flex;
    align-items: center;
    justify-content: center;
    gap: 14px;
  }
  .emblem-name {
    font-family: "Arimo", Arial, sans-serif;
    font-weight: 700;
    font-size: 40px;
    letter-spacing: 4px;
    color: var(--type-dark);
  }
  .emblem-square {
    width: 18px;
    height: 18px;
    background: var(--type-dark);
  }
  .face-brand-zone {
    flex: 1;
    background: var(--panel-black);
    display: flex;
    align-items: center;
    justify-content: center;
  }
  .brand-name {
    font-family: "Arimo", Arial, sans-serif;
    font-weight: 700;
    font-size: 118px;
    letter-spacing: 14px;
    color: var(--type-light);
    line-height: 1;
  }
</style>
</head>
<body>
  <main class="canvas">
    <section class="box-face box-face--top">
      <div class="face-emblem-zone">
        <span class="emblem-square"></span>
        <span class="emblem-name">K.E.L.T</span>
      </div>
      <div class="face-brand-zone">
        <h1 class="brand-name">K.E.L.T</h1>
      </div>
    </section>
    <section class="box-face box-face--front">
      <div class="face-emblem-zone">
        <span class="emblem-square"></span>
        <span class="emblem-name">K.E.L.T</span>
      </div>
      <div class="face-brand-zone">
        <p class="brand-name">K.E.L.T</p>
      </div>
    </section>
  </main>
</body>
</html>
```